Velora Aesthetica

Medical doctor providing aesthetic medicine

* Double sided card
* Logo to be on card
Other details:
* Dr. Mirela Kostvan, BSc, MBChB, CCFP
* #214-215, 27903 83 Ave, Surrey, BC, V2T 4K7
* 604-718-2943
* info@veloraclinic.ca
* www.veloraclinic.ca

Industry/Entity Type

Medical / Health & Beauty

Contact Information for Business Card

see 'Project Description'

Colors
0054AA
0677BA
7BADD7
CADEEF
E8F1F8
FFF300
FFF600
FEFA6F
FFFEC7
FFFEE8

Requirements
Must have
• Modern, high-end design

```html
<!DOCTYPE html>
<html lang="en">
<head>
<meta charset="utf-8">
<title>Velora Aesthetica – Business Card</title>
<link rel="stylesheet" href="https://fonts.googleapis.com/css2?family=Poppins:wght@400;500;700&family=Montserrat:wght@500;600&display=swap">
<style>
  :root {
    --backdrop: #2b2b2b;
    --paper: #ffffff;
    --ink: #111111;
    --gold: #c9a227;
    --gold-light: #e6bf2f;
    --card-black: #050505;
    --rule: #222222;
  }
  * { box-sizing: border-box; margin: 0; padding: 0; }
  html, body {
    width: 1200px; height: 900px; overflow: hidden;
    background: var(--backdrop);
  }
  .canvas {
    width: 1200px; height: 900px;
    display: flex; flex-direction: column; align-items: center; justify-content: center;
    gap: 40px;
  }
  .card {
    position: relative;
    width: 700px; height: 400px;
    overflow: hidden;
    box-shadow: 0 14px 30px rgba(0,0,0,.45);
  }

  /* Front */
  .card--front { background: var(--paper); }
  .front__band {
    position: absolute; left: 0; right: 0; bottom: 0; height: 20px;
    background: linear-gradient(90deg, var(--gold), var(--gold-light));
  }
  .holder {
    position: absolute; left: 52px; top: 96px;
    font-family: "Poppins", sans-serif;
  }
  .holder__name {
    font-weight: 700; font-size: 30px; letter-spacing: .5px; color: var(--ink);
    text-transform: uppercase; line-height: 1.1;
  }
  .holder__creds {
    font-weight: 400; font-size: 19px; color: var(--gold); margin-top: 2px;
  }
  .brand {
    position: absolute; right: 60px; top: 70px;
    display: flex; align-items: center; gap: 12px;
    font-family: "Montserrat", sans-serif; font-weight: 600;
    font-size: 24px; letter-spacing: 3px; text-transform: uppercase; color: var(--ink);
  }
  .brand__dot {
    width: 18px; height: 18px; border-radius: 50%; background: var(--gold);
  }
  .front__rule {
    position: absolute; left: 52px; right: 52px; top: 236px;
    height: 1px; background: var(--rule);
  }
  .contact {
    position: absolute; left: 52px; top: 252px;
    list-style: none;
    font-family: "Poppins", sans-serif; font-size: 16px; color: var(--ink);
  }
  .contact__item { display: flex; align-items: center; gap: 10px; line-height: 30px; }
  .contact__icon { width: 16px; height: 16px; flex: none; }
  .address {
    position: absolute; right: 52px; top: 250px;
    font-family: "Poppins", sans-serif; font-size: 15px; color: var(--ink);
  }

  /* Back */
  .card--back { background: var(--card-black); }
  .back__brand {
    position: absolute; left: 0; right: 0; top: 150px;
    display: flex; align-items: center; justify-content: center; gap: 16px;
    font-family: "Montserrat", sans-serif; font-weight: 600;
    font-size: 38px; letter-spacing: 5px; text-transform: uppercase; color: var(--gold-light);
  }
  .back__brand .brand__dot { width: 26px; height: 26px; background: var(--gold-light); }
  .back__web {
    position: absolute; left: 0; right: 0; top: 300px; text-align: center;
    font-family: "Montserrat", sans-serif; font-weight: 500;
    font-size: 18px; letter-spacing: 7px; text-transform: uppercase; color: #ffffff;
  }
</style>
</head>
<body>
<main class="canvas">
  <section class="card card--front" aria-label="Card front">
    <div class="holder">
      <h1 class="holder__name">Dr. Mirela Kostvan</h1>
      <p class="holder__creds">BSc, MBChB, CCFP</p>
    </div>
    <div class="brand"><span class="brand__dot"></span>Velora Aesthetica</div>
    <div class="front__rule"></div>
    <ul class="contact">
      <li class="contact__item">
        <svg class="contact__icon" viewBox="0 0 24 24" aria-hidden="true"><path fill="#c9a227" d="M6.6 10.8a15 15 0 0 0 6.6 6.6l2.2-2.2c.3-.3.7-.4 1-.2 1.1.4 2.3.6 3.6.6.6 0 1 .4 1 1V20c0 .6-.4 1-1 1A17 17 0 0 1 3 4c0-.6.4-1 1-1h3.5c.6 0 1 .4 1 1 0 1.3.2 2.5.6 3.6.1.3 0 .7-.2 1z"/></svg>
        604-718-2943
      </li>
      <li class="contact__item">
        <svg class="contact__icon" viewBox="0 0 24 24" aria-hidden="true"><rect x="2" y="5" width="20" height="14" fill="#c9a227"/><path d="M2 5l10 8 10-8" fill="none" stroke="#fff" stroke-width="1.6"/></svg>
        info@veloraclinic.ca
      </li>
      <li class="contact__item">
        <svg class="contact__icon" viewBox="0 0 24 24" aria-hidden="true"><g fill="none" stroke="#c9a227" stroke-width="2"><circle cx="12" cy="12" r="9"/><path d="M3 12h18M12 3c3 3 3 15 0 18M12 3c-3 3-3 15 0 18"/></g></svg>
        www.veloraclinic.ca
      </li>
    </ul>
    <p class="address">#214-215, 27903 83 Ave, Surrey, BC, V2T 4K7</p>
    <div class="front__band"></div>
  </section>

  <section class="card card--back" aria-label="Card back">
    <div class="back__brand"><span class="brand__dot"></span>Velora Aesthetica</div>
    <p class="back__web">www.veloraclinic.ca</p>
  </section>
</main>
</body>
</html>
```